Do i have coronavirus, flue or cold?

Using information from QRV and government agencies we want to make a easy to read infographic helping patients see if they have coronavirus, the flu or a cold. Using a flow diagram or whatever you think will make it easy to read and digest for the average lamen.

Information is in the word document and in the chart.

We are www.tovipharm.co.uk attached is our brand guidelines, we will be putting this infographic on our website and email/sms it to all of our 300,000 patients.

```html
<!DOCTYPE html>
<html lang="en">
<head>
<meta charset="utf-8">
<title>Tovipharm – Medicine delivered discreetly</title>
<link href="https://fonts.googleapis.com/css2?family=Nunito+Sans:wght@300;400;600;700&display=swap" rel="stylesheet">
<style>
:root{
  --stage:#03032e;
  --page:#edf3f6;
  --page-tint:#e0eaf1;
  --white:#ffffff;
  --ink:#0d0f3a;
  --ink-soft:#2a2d55;
  --accent:#7f96ee;
  --btn-dark:#3333b5;
  --btn-light:#7d91f0;
  --rule:#d9e2ea;
  --score:#00b67a;
  --badge:#f26a2a;
}
*{margin:0;padding:0;box-sizing:border-box}
html,body{width:1200px;height:1200px;overflow:hidden;background:var(--stage);font-family:"Nunito Sans",sans-serif;color:var(--ink)}
.page{position:absolute;left:18px;top:191px;width:1163px;height:817px;background:var(--page);overflow:hidden}
.page-tint{position:absolute;left:0;top:0}
.lower{position:absolute;left:0;top:587px;width:100%;height:230px;background:var(--white)}
.abs{position:absolute}
.header{left:97px;top:0;width:970px;height:66px;background:var(--white)}
.brand{left:14px;top:23px;display:flex;align-items:center;gap:6px;font-weight:600;font-size:16px;line-height:20px;color:var(--btn-dark);white-space:nowrap}
.brand-dot{width:18px;height:18px;border-radius:50%;background:var(--btn-light);flex:none}
.search{left:123px;top:12px;width:506px;height:39px;border:1px solid var(--rule);border-radius:3px;font-size:11px;padding:12px 18px;color:var(--ink)}
.search svg{position:absolute;right:14px;top:10px}
.tool{top:14px;text-align:center;font-size:11px;color:var(--ink-soft);width:80px}
.tool svg{display:block;margin:0 auto 4px}
.divider-v{left:878px;top:0;width:1px;height:66px;background:var(--rule)}
.count{right:-2px;top:-4px;width:17px;height:17px;border-radius:50%;background:var(--badge);color:#fff;font-size:10px;line-height:17px;text-align:center}
.nav{left:97px;top:83px;width:970px;display:flex;justify-content:space-between;font-size:11.5px;color:var(--ink-soft)}
.hero-title{left:96px;top:188px;font-weight:300;font-size:35px;line-height:42px;color:var(--ink)}
.hero-title em{font-style:normal;color:var(--accent)}
.hero-copy{left:97px;top:290px;width:340px;font-size:13px;line-height:19.5px;color:var(--ink-soft)}
.rating{left:97px;top:367px;display:flex;align-items:center;gap:18px;font-size:12.5px}
.squares{display:flex;gap:2px}
.squares span{width:24px;height:24px;background:var(--score)}
.rating-brand{display:flex;align-items:center;gap:5px;font-weight:600;font-size:13px}
.rating-brand i{width:12px;height:12px;background:var(--score)}
.score{left:97px;top:397px;font-size:9px;color:var(--ink-soft)}
.btn{top:437px;height:39px;color:#fff;font-size:12px;line-height:39px;text-align:center}
.btn-dark{left:97px;width:161px;background:var(--btn-dark)}
.btn-light{left:274px;width:174px;background:var(--btn-light)}
.figure{left:468px;top:241px;width:146px;height:237px;background:linear-gradient(180deg,#f3c9b6 0%,#f0b8a4 40%,#6f86e6 60%,#4b5fd0 100%);border-radius:60px 60px 6px 6px}
.chart{left:0;top:0}
.steps .num{top:565px;width:41px;height:41px;border-radius:50%;background:var(--white);border:1px solid var(--rule);font-size:16px;line-height:39px;text-align:center}
.steps .num.active{background:var(--btn-light);border-color:var(--btn-light);color:#fff}
.step-line{left:137px;top:585px;width:177px;height:2px;background:var(--btn-light)}
.step h3{font-weight:400;font-size:18px;margin-bottom:9px}
.step p{font-size:13px;line-height:19.5px;color:var(--ink-soft);width:258px}
.step{top:643px}
.foot-rule{left:97px;top:762px;width:970px;height:1px;background:var(--rule)}
</style>
</head>
<body>
<main class="page">
  <svg class="page-tint" width="1163" height="587" viewBox="0 0 1163 587" aria-hidden="true">
    <path d="M1163 60 L820 60 C760 140 800 300 700 380 C600 460 380 420 300 587 L1163 587 Z" fill="var(--page-tint)"/>
  </svg>
  <div class="lower"></div>

  <header class="abs header">
    <div class="abs brand"><span class="brand-dot"></span>Tovipharm</div>
    <div class="abs search">Search treatments
      <svg width="17" height="17" viewBox="0 0 17 17" fill="none" stroke="var(--ink)" stroke-width="1.5"><circle cx="7" cy="7" r="5.5"/><line x1="11" y1="11" x2="16" y2="16"/></svg>
    </div>
    <div class="abs tool" style="left:669px">
      <svg width="18" height="16" viewBox="0 0 18 16" fill="none" stroke="var(--ink)" stroke-width="1.3"><rect x="1" y="3" width="16" height="12" rx="2"/><path d="M6 3V1h6v2M9 6v6M6 9h6"/></svg>How it works</div>
    <div class="abs tool" style="left:744px">
      <svg width="17" height="17" viewBox="0 0 17 17" fill="none" stroke="var(--ink)" stroke-width="1.3"><circle cx="8.5" cy="8.5" r="7.5"/><circle cx="8.5" cy="8.5" r="3"/><path d="M3 3l3.5 3.5M14 3l-3.5 3.5M3 14l3.5-3.5M14 14l-3.5-3.5"/></svg>Help</div>
    <div class="abs tool" style="left:807px">
      <svg width="17" height="17" viewBox="0 0 17 17" fill="none" stroke="var(--ink)" stroke-width="1.3"><circle cx="8.5" cy="8.5" r="7.5"/><circle cx="8.5" cy="7" r="2.6"/><path d="M4 14c1-2.5 8-2.5 9 0"/></svg>Account</div>
    <div class="abs divider-v"></div>
    <div class="abs tool" style="left:903px">
      <svg width="18" height="16" viewBox="0 0 18 16" fill="none" stroke="var(--ink)" stroke-width="1.3"><path d="M1 6h16l-2 9H3z"/><path d="M5 6l4-5 4 5M6 9v4M9 9v4M12 9v4"/></svg>Basket
      <span class="abs count">3</span></div>
  </header>

  <nav class="abs nav">
    <span>Men’s Health</span><span>Women’s Health</span><span>Chronic Conditions</span><span>Sexual</span><span>Travel</span><span>Wellbeing</span><span>General</span><span>Vitamins &amp; Supplements</span><span>Tests &amp; Diagnostics</span>
  </nav>

  <h1 class="abs hero-title">Medicine delivered<br><em>discreetly</em> to your door</h1>
  <p class="abs hero-copy">Get UK medicines delivered to your door in as little as a few hours as you would from your GP - no queues, no wait, no stress.</p>
  <div class="abs rating">
    <div class="squares"><span></span><span></span><span></span><span></span><span></span></div>
    <span>Rated “Excellent”</span>
    <span class="rating-brand"><i></i>Revuo</span>
  </div>
  <div class="abs score">Score 9 – 6,035 reviews</div>
  <div class="abs btn btn-dark">View all products A-Z</div>
  <div class="abs btn btn-light">View all treatments A-Z</div>

  <div class="abs figure" role="img" aria-label="Illustration of an unwell person with a cold compress on the forehead, coughing, with symptom areas marked"></div>

  <svg class="abs chart" width="1163" height="587" viewBox="0 0 1163 587" font-family="Nunito Sans, sans-serif" fill="var(--ink)">
    <text x="458" y="208" font-size="16" font-weight="700">Do I have coronavirus,</text>
    <text x="458" y="228" font-size="16" font-weight="700">the flu or a cold?</text>
    <g stroke="var(--white)" stroke-width="2">
      <line x1="641" y1="189" x2="641" y2="485"/><line x1="764" y1="189" x2="764" y2="485"/>
      <line x1="864" y1="189" x2="864" y2="485"/><line x1="964" y1="189" x2="964" y2="485"/>
      <g stroke-width="1.5">
        <line x1="440" y1="231" x2="1065" y2="231"/><line x1="641" y1="254" x2="1065" y2="254"/>
        <line x1="641" y1="278" x2="1065" y2="278"/><line x1="641" y1="324" x2="1065" y2="324"/>
        <line x1="641" y1="339" x2="1065" y2="339"/><line x1="641" y1="354" x2="1065" y2="354"/>
        <line x1="641" y1="368" x2="1065" y2="368"/><line x1="641" y1="383" x2="1065" y2="383"/>
        <line x1="641" y1="419" x2="1065" y2="419"/>
      </g>
    </g>
    <g font-size="12" font-weight="700" text-anchor="middle">
      <text x="701" y="216">SYMPTOM</text><text x="814" y="216">CORONAVIRUS</text>
      <text x="914" y="216">FLU</text><text x="1015" y="216">COLD</text>
    </g>
    <g stroke="var(--ink)" stroke-width="1" stroke-dasharray="1 2">
      <line x1="520" y1="243" x2="641" y2="243"/><line x1="610" y1="265" x2="641" y2="265"/>
      <line x1="575" y1="300" x2="641" y2="300"/><line x1="580" y1="331" x2="641" y2="331"/>
      <line x1="580" y1="346" x2="641" y2="346"/><line x1="585" y1="360" x2="641" y2="360"/>
      <line x1="598" y1="375" x2="641" y2="375"/><line x1="605" y1="401" x2="641" y2="401"/>
      <line x1="595" y1="429" x2="641" y2="429"/>
    </g>
    <g>
      <circle cx="641" cy="243" r="2"/><circle cx="641" cy="265" r="2"/><circle cx="641" cy="300" r="2"/>
      <circle cx="641" cy="331" r="2"/><circle cx="641" cy="346" r="2"/><circle cx="641" cy="360" r="2"/>
      <circle cx="641" cy="375" r="2"/><circle cx="641" cy="401" r="2"/><circle cx="641" cy="429" r="2"/>
    </g>
    <g font-size="11.5">
      <text x="649" y="247">Tiredness</text><text x="649" y="269">Headache</text><text x="649" y="304">Fever</text>
      <text x="649" y="335">Sneezing</text><text x="649" y="350">Stuffy or runny nose</text><text x="649" y="364">Cough</text>
      <text x="649" y="379">Sore throat</text><text x="649" y="405">Muscle aches</text><text x="649" y="433">Shortness of breath</text>
    </g>
    <g font-size="11.5" text-anchor="middle">
      <text x="814" y="247">YES</text><text x="914" y="247">YES</text><text x="1015" y="247">Mild</text>
      <text x="814" y="269">Sometimes</text><text x="914" y="269">YES</text><text x="1015" y="269">Rare</text>
      <text x="814" y="304">YES</text><text x="914" y="304">YES <tspan font-size="7.5" font-style="italic">(High)</tspan></text><text x="1015" y="304">Rare</text>
      <text x="814" y="335">NO</text><text x="914" y="335">Sometimes</text><text x="1015" y="335">YES</text>
      <text x="814" y="350">Rare</text><text x="914" y="350">Sometimes</text><text x="1015" y="350">YES</text>
      <text x="814" y="364">YES <tspan font-size="7.5" font-style="italic">(Dry cough)</tspan></text><text x="914" y="364">YES</text><text x="1015" y="364">Moderate</text>
      <text x="814" y="379">Sometimes</text><text x="914" y="379">Sometimes</text><text x="1015" y="379">YES</text>
      <text x="814" y="405">YES</text><text x="914" y="405">YES <tspan font-size="7.5" font-style="italic">(Often)</tspan></text><text x="1015" y="405">Moderate</text>
      <text x="814" y="433">YES</text><text x="914" y="433">YES</text><text x="1015" y="433">Rare</text>
    </g>
  </svg>

  <section class="steps">
    <div class="abs step-line"></div>
    <div class="abs num active" style="left:97px">1</div>
    <div class="abs num" style="left:429px">2</div>
    <div class="abs num" style="left:761px">3</div>
    <div class="abs step" style="left:97px"><h3>Choose your treatment</h3><p>Sit back, relax and choose your one-off or subscription of medication on any device from anywhere.</p></div>
    <div class="abs step" style="left:428px"><h3>Complete a consultation</h3><p>With complete privacy and confidentiality your form is checked by one of our UK partner doctors.</p></div>
    <div class="abs step" style="left:759px"><h3>Recieve your delivery</h3><p>With same day service in parts of the UK, you can have your treatment delivery discreetly within hours.</p></div>
  </section>
  <div class="abs foot-rule"></div>
</main>
</body>
</html>
```